I need to re design my current Business Proposal , More professional and beautiful

We currently use a power point template to create our business proposal for construction projects ,we use powerpoint to create the template then we export to PDF.

i like it but i think it can be better, i will upload our current powerpoint template, PDF Example, Our Company Brochure (so you can see the level of design we are expecting.

Page 1 - Front Cover ( make sure you incorporate the picture of all the techs) -------REDESIGN
Page 2 - Introduction Page - PLEASE SIMPLE DETAILS
Page 3 - Scope of Work - PLEASE SIMPLE DETAILS
Page 4 - Classification and Exclusion Page- PLEASE SIMPLE DETAILS
Page 5 Pricing - PLEASE SIMPLE DETAILS
Page 6 - Payment Schedule - PLEASE SIMPLE DETAILS
Page 7 References -----REDESIGN
Page 8 Recent Projects-----REDESIGN
Page 9 Certification and lets add the brand logos of Manufacturer we work with ( see brochure) -----REDESIGN

Also here is google drive link with some pictures
https://filebox-share.example/folders/7kqum_RRTwhq92P47WvxFm4-Lh3j?usp=sharing

also you can download more pics from our website

rilvenbuilders.com

```html
<!DOCTYPE html>
<html lang="en">
<head>
<meta charset="utf-8">
<title>Rilven Builders – Proposal Slide Set</title>
<link rel="stylesheet" href="https://fonts.googleapis.com/css2?family=Arimo:wght@400;700&family=Dancing+Script:wght@600&family=Michroma&family=Raleway:wght@200&display=swap">
<style>
  :root{
    --board:#8b8c90;
    --white:#ffffff;
    --navy:#0a2d66;
    --blue:#1663b0;
    --cyan:#1ba8e2;
    --ice:#a9ddf4;
    --ink:#222a33;
    --muted:#5b6470;
    --green:#7cc242;
    --yellow:#f5c816;
    --orange:#f47b20;
    --red:#e23b2e;
    --gray-tab:#b4b6b9;
    --display:"Michroma",sans-serif;
    --body:"Arimo",sans-serif;
  }
  *{box-sizing:border-box;margin:0;padding:0}
  html,body{width:1200px;height:903px;overflow:hidden;background:var(--board)}
  .board{position:relative;width:1200px;height:903px;background:var(--board);font-family:var(--body);color:var(--ink)}
  .board-title{position:absolute;top:18px;left:0;width:1200px;text-align:center;font-family:"Raleway",sans-serif;font-weight:200;font-size:41px;letter-spacing:1px;color:var(--white)}

  .slide{position:absolute;width:296px;height:209px;background:var(--white);overflow:hidden;box-shadow:0 5px 12px rgba(0,0,0,.32)}
  .col-1{left:85px}.col-2{left:452px}.col-3{left:819px}
  .row-1{top:89px}.row-2{top:362px}.row-3{top:636px}

  .brand{position:absolute;left:9px;top:3px;text-align:center;line-height:1}
  .brand-mark{display:block;width:6px;height:6px;margin:0 auto 1px;background:var(--blue)}
  .brand-name{display:block;font-family:var(--display);font-size:3.6px;color:var(--navy)}
  .header-band{position:absolute;left:54px;top:0;right:0;height:15px;background:linear-gradient(90deg,var(--navy),var(--blue) 50%,var(--cyan));clip-path:polygon(8px 0,100% 0,100% 100%,0 100%)}
  .header-title{position:absolute;left:74px;top:4.6px;font-family:var(--display);font-size:5.6px;color:var(--white);letter-spacing:.2px;white-space:nowrap}
  .accent-stripes{position:absolute;left:94px;top:15px;display:flex;gap:1.4px}
  .accent-stripes span{display:block;width:2.2px;height:5.5px;transform:skewX(-32deg)}
  .s-red{background:var(--red)}.s-orange{background:var(--orange)}.s-yellow{background:var(--yellow)}.s-green{background:var(--green)}
  .footer-bar{position:absolute;left:0;bottom:0;width:242px;height:6px;background:linear-gradient(90deg,var(--cyan),var(--blue) 65%,var(--navy));clip-path:polygon(0 0,100% 0,calc(100% - 4px) 100%,0 100%)}
  .footer-tab{position:absolute;right:0;bottom:0;width:58px;height:10px;background:linear-gradient(180deg,#e1e2e3,var(--gray-tab));clip-path:polygon(8px 0,100% 0,100% 100%,0 100%)}

  .bullets{position:absolute;list-style:none}
  .bullets li{position:absolute;left:0;padding-left:8px;font-size:4.4px;line-height:5.2px;width:100%}
  .bullets li::before{content:"";position:absolute;left:0;top:2px;width:1.6px;height:1.6px;background:var(--ink)}

  .cover{background:linear-gradient(140deg,#0e56a0 0%,#0b3c7e 45%,#092a60 100%)}
  .cover-photo{position:absolute;left:0;top:0;width:296px;height:209px;background:linear-gradient(180deg,#bfd6ea 0%,#e8eef3 30%,#2c3f66 55%,#5a5c63 80%,#2f3138 100%);clip-path:polygon(236px 32px,296px 32px,296px 180px,148px 180px)}
  .cover-stripes{position:absolute;left:0;top:0}
  .cover-brand{position:absolute;left:12px;top:30px;width:76px;text-align:center}
  .cover-brand .brand-mark{width:12px;height:12px;background:var(--cyan);margin-bottom:4px}
  .cover-brand .brand-name{font-size:6.4px;color:var(--white);letter-spacing:.4px}
  .cover-title{position:absolute;left:11px;top:73px;font-family:var(--display);font-size:18.5px;color:var(--white);letter-spacing:.5px}
  .cover-for{position:absolute;left:12px;top:98px;font-family:var(--display);font-size:7.4px;color:var(--white)}
  .cover-rule{position:absolute;left:27px;top:105px;width:216px;height:.5px;background:rgba(255,255,255,.55)}
  .cover-fields{position:absolute;left:12px;top:120px;width:113px;border-collapse:collapse}
  .cover-fields td{height:8.5px;border:.5px solid rgba(255,255,255,.6);font-size:3.9px;color:var(--white);padding:0 3px;vertical-align:middle}
  .cover-fields td:first-child{width:54px}
  .cover-offices{position:absolute;left:12px;top:188px;font-family:var(--display);font-size:3.7px;color:var(--white)}
  .cover-notice-panel{position:absolute;left:0;top:0;width:296px;height:209px;background:linear-gradient(180deg,#eef0f2,#d9dcdf);clip-path:polygon(160px 180px,296px 180px,296px 209px,142px 209px)}
  .cover-notice{position:absolute;left:170px;top:185px;width:118px;color:#3a3f46}
  .cover-notice h4{font-size:2.9px;font-weight:700;margin-bottom:1.2px}
  .cover-notice p{font-size:2.3px;line-height:2.9px}

  .letter{position:absolute;left:39px;top:40px;width:218px}
  .letter p{font-size:4.1px;line-height:5px;text-align:justify;margin-bottom:4.4px}
  .signature{font-family:"Dancing Script",cursive;font-size:5.4px;color:var(--ink)}

  .price-table{position:absolute;left:42px;top:33px;width:212px;height:131px;border:.6px solid #8a96a3}
  .price-table .th{position:absolute;left:0;top:0;right:0;height:11px;background:var(--cyan);color:var(--white);font-family:var(--display);font-size:4.2px;line-height:11px;padding-left:6px}
  .price-table .divider{position:absolute;left:176px;top:0;bottom:0;width:.6px;background:#8a96a3}
  .price-total{position:absolute;left:131px;top:170px;width:123px;height:13px;background:var(--ice);border:.6px solid #5c7f98;font-size:3.9px;line-height:12px;padding-left:6px}
  .price-total .divider{position:absolute;left:86px;top:0;bottom:0;width:.6px;background:#5c7f98}

  .pay-note{position:absolute;left:42px;top:66px;width:212px;font-size:4.1px;line-height:5px}
  .signed-label{position:absolute;left:43px;top:95px;font-family:var(--body);font-weight:700;font-size:5.6px;color:var(--cyan);letter-spacing:.2px}
  .signed-rule{position:absolute;left:43px;top:104px;width:210px;height:.6px;background:#8a96a3}
  .sig-line{position:absolute;height:.5px;background:#b7bec6}
  .sig-label{position:absolute;font-size:4px;line-height:5px}

  .section-band{position:absolute;left:0;height:11px;width:146px;background:var(--cyan);clip-path:polygon(0 0,100% 0,calc(100% - 6px) 100%,0 100%)}
  .section-band-stripes{position:absolute;left:8px;display:flex;gap:1.6px}
  .section-band-stripes span{display:block;width:2.6px;height:11px;transform:skewX(-32deg)}
  .band-label{position:absolute;font-family:var(--display);font-size:4.6px;color:var(--white)}
  .ref{position:absolute;width:110px}
  .ref h5{font-family:var(--display);font-size:3.7px;color:var(--navy);margin-bottom:1.2px}
  .ref p{font-size:3.2px;line-height:4.1px;color:#2c3d66;padding-left:5px;position:relative}
  .ref p.i::before{content:"";position:absolute;left:.6px;top:1.2px;width:1.7px;height:1.7px;border-radius:50%;background:var(--cyan)}
  .client-strip{position:absolute;left:38px;top:180px;width:222px;display:flex;justify-content:space-between;align-items:center}
  .client-strip span{font-size:3.4px;font-weight:700;color:#4b5563;display:flex;align-items:center;gap:1.2px}
  .client-strip span i{display:block;width:3px;height:3px;background:#9aa3ad}

  .project-grid{position:absolute;left:35px;top:46px;width:228px;display:grid;grid-template-columns:repeat(6,36.5px);column-gap:1.8px;row-gap:3.6px;grid-template-rows:22px 31px 31px 31px}
  .project-head{background:var(--navy);color:var(--white);font-size:3.1px;line-height:3.7px;display:flex;align-items:center;justify-content:center;text-align:center;padding:0 1.5px;border-radius:1px}
  .project-photo{border-radius:1.5px}
  .ph-a{background:linear-gradient(160deg,#9aa7b6,#3c4a60)}
  .ph-b{background:linear-gradient(160deg,#2d3440,#6f7a88)}
  .ph-c{background:linear-gradient(160deg,#c7ced6,#6b7480)}
  .ph-d{background:linear-gradient(160deg,#8e4aa0,#3a2a58)}
  .ph-e{background:linear-gradient(160deg,#1f2530,#b3463c)}
  .ph-f{background:linear-gradient(160deg,#5b8f5a,#2b3a48)}

  .cert-copy{position:absolute;left:44px;top:46px;width:95px;font-size:3.55px;line-height:4.55px;color:#2c3038}
  .cert-intro{position:absolute;left:45px;top:130px;font-size:3px;color:#2c3038}
  .partner-row{position:absolute;left:45px;display:flex;gap:9px}
  .partner-row span{font-size:4.6px;font-weight:700;color:#1b2230;display:flex;align-items:center;gap:1.5px}
  .partner-row span i{display:block;width:3.4px;height:3.4px;background:#1b2230}
  .cert-photo{position:absolute;left:163px;top:46px;width:88px;height:118px;border-radius:4px;background:linear-gradient(160deg,#e4e4e2 0%,#6d7380 45%,#2f3440 75%,#c9c7c2 100%)}
</style>
</head>
<body>
<main class="board">
  <h1 class="board-title">POWERPOINT DESIGN</h1>

  <section class="slide cover col-1 row-1">
    <div class="cover-photo" role="img" aria-label="Team photo of the installation technicians standing in front of the company vans"></div>
    <svg class="cover-stripes" width="296" height="209" viewBox="0 0 296 209" aria-hidden="true">
      <polygon points="273,0 296,0 296,16 262,72 240,72" fill="#ffffff"/>
      <polygon points="190,120 206,120 195,138 179,138" fill="#1ba8e2" opacity=".9"/>
      <polygon points="277,2 283,2 242,70 236,70" fill="var(--green)"/>
      <polygon points="270,2 276,2 235,70 229,70" fill="var(--yellow)"/>
      <polygon points="263,2 269,2 228,70 222,70" fill="var(--orange)"/>
      <polygon points="256,2 262,2 221,70 215,70" fill="var(--red)"/>
      <polygon points="249,2 255,2 214,70 208,70" fill="var(--cyan)"/>
      <polygon points="122,160 140,160 112,209 94,209" fill="var(--cyan)"/>
      <polygon points="138,170 146,170 122,209 114,209" fill="#5fc4ee"/>
      <polygon points="148,152 156,152 137,182 129,182" fill="#0e56a0"/>
    </svg>
    <div class="cover-notice-panel"></div>
    <div class="cover-brand"><span class="brand-mark"></span><span class="brand-name">RILVEN BUILDERS</span></div>
    <div class="cover-title">PROPOSAL</div>
    <div class="cover-for">For</div>
    <div class="cover-rule"></div>
    <table class="cover-fields">
      <tr><td>RB Contract Name:</td><td></td></tr>
      <tr><td>Property Location:</td><td></td></tr>
      <tr><td>Proposal Description:</td><td></td></tr>
      <tr><td>Date of Proposal:</td><td></td></tr>
      <tr><td>ATTN:</td><td></td></tr>
      <tr><td>Quote#</td><td></td></tr>
    </table>
    <div class="cover-offices">Offices Harborview - Cedar Point - Lakeshore</div>
    <div class="cover-notice">
      <h4>NOTICE OF PROPRIETARY INFORMATION</h4>
      <p>THE CONTENTS OF THIS PACKAGE ARE CONSIDERED BY RILVEN BUILDERS TO BE PROPRIETARY. THIS DOCUMENT IS INTENDED FOR THE SOLE USE OF THE CUSTOMER AND MAY NOT BE RELEASED TO ANY OTHER VENDOR OR CONTRACTOR WITHOUT WRITTEN PERMISSION FROM RILVEN BUILDERS.</p>
    </div>
  </section>

  <section class="slide col-2 row-1">
    <div class="brand"><span class="brand-mark"></span><span class="brand-name">RILVEN BUILDERS</span></div>
    <div class="header-band"></div><div class="header-title">INTRODUCTION</div>
    <div class="accent-stripes"><span class="s-red"></span><span class="s-orange"></span><span class="s-yellow"></span><span class="s-green"></span></div>
    <div class="letter">
      <p>October 31, 2023</p>
      <p style="margin-top:8px">Dear Mr. Dana Whitfield,</p>
      <p>Thank you for providing us with the opportunity to present this Proposal addressing your Structured cabling needs.</p>
      <p>For over 15 years, Rilven Builders has provided excellent low voltage services and solutions for organizations and commercial clients in the Gulf Coast region. We have successfully completed thousands of structured cabling projects for offices, retail centers, churches, and schools. We stand by our work and guarantee excellent quality and materials. We adhere to safety standards and meet all safety regulations of the state.</p>
      <p>Included in this proposal, you will find a complete solution designed to meet your structured cabling needs. We know time is of the essence, so please don't hesitate to contact me with any further questions.</p>
      <p>Thank again for considering Rilven Builders as your partner for your Structured cabling needs.</p>
      <p>We look forward to working with you.</p>
      <p>Sincerely,</p>
      <p class="signature">Leo Marchetti</p>
    </div>
    <div class="footer-bar"></div><div class="footer-tab"></div>
  </section>

  <section class="slide col-3 row-1">
    <div class="brand"><span class="brand-mark"></span><span class="brand-name">RILVEN BUILDERS</span></div>
    <div class="header-band"></div><div class="header-title">SCOPE OF WORK</div>
    <div class="accent-stripes"><span class="s-red"></span><span class="s-orange"></span><span class="s-yellow"></span><span class="s-green"></span></div>
    <ul class="bullets" style="left:39px;top:0;width:222px;height:209px">
      <li style="top:41px">Rilven will Label every cable for easy identification</li>
      <li style="top:58px">Rilven will test , and label all the cabling and terminations</li>
      <li style="top:74px">Rilven will follow State low voltage Code installation procedures, and also follow best practices and guidelines by TCA (Telecom Cabling Alliance)</li>
      <li style="top:96px">Rilven will dressed the cables and terminate them in clean organized way.</li>
      <li style="top:113px">2 Year Labor Warranty / 15 Manufacturer Warranty</li>
    </ul>
    <div class="footer-bar"></div><div class="footer-tab"></div>
  </section>

  <section class="slide col-1 row-2">
    <div class="brand"><span class="brand-mark"></span><span class="brand-name">RILVEN BUILDERS</span></div>
    <div class="header-band"></div><div class="header-title">Clarifications and Exclusion</div>
    <div class="accent-stripes"><span class="s-red"></span><span class="s-orange"></span><span class="s-yellow"></span><span class="s-green"></span></div>
    <ul class="bullets" style="left:40px;top:0;width:218px;height:209px">
      <li style="top:39px">Rilven will install materials that meet / exceeds the highest performance and durability standards. All the materials will carry a recognized safety Listing.</li>
      <li style="top:60px">All conduit, junction boxes, fittings and Stub ups will be provided by others.</li>
      <li style="top:76px">Rilven will follow State low voltage Code installation procedures, and also follow best practices and guidelines by TCA (Telecom Cabling Alliance) .</li>
      <li style="top:97px">Rilven will dressed the cables and terminate them in clean organized way.</li>
      <li style="top:112px">2 Year Labor Warranty / 15 Manufacturer Warranty .</li>
      <li style="top:125px">Customer to provide electronic DraftPlan files for our use in creating submittal drawings ( As Built Drawings).</li>
      <li style="top:143px">Permits or associated fees are not included.</li>
      <li style="top:156px">Customer to provide a secured staging &amp; storage area for project related materials.</li>
      <li style="top:172px">All work proposed herein, shall be performed during normal business hours Monday- Friday.</li>
    </ul>
    <div class="footer-bar"></div><div class="footer-tab"></div>
  </section>

  <section class="slide col-2 row-2">
    <div class="brand"><span class="brand-mark"></span><span class="brand-name">RILVEN BUILDERS</span></div>
    <div class="header-band"></div><div class="header-title">PRICING</div>
    <div class="accent-stripes"><span class="s-red"></span><span class="s-orange"></span><span class="s-yellow"></span><span class="s-green"></span></div>
    <div class="price-table"><div class="th">Materials &amp; Labor</div><div class="divider"></div></div>
    <div class="price-total">Total Project Cost<div class="divider"></div></div>
    <div class="footer-bar"></div><div class="footer-tab"></div>
  </section>

  <section class="slide col-3 row-2">
    <div class="brand"><span class="brand-mark"></span><span class="brand-name">RILVEN BUILDERS</span></div>
    <div class="header-band"></div><div class="header-title">PAYMENT SCHEDULE</div>
    <div class="accent-stripes"><span class="s-red"></span><span class="s-orange"></span><span class="s-yellow"></span><span class="s-green"></span></div>
    <ul class="bullets" style="left:44px;top:0;width:212px;height:209px">
      <li style="top:36px;font-size:4.1px;line-height:5px">Fifteen Percent(15%) of the proposed sell price shall be payable to Rilven Builders for project mobilization.</li>
      <li style="top:53px;font-size:4.1px">Balance (85%) due upon completion of the Project.</li>
    </ul>
    <p class="pay-note">We appreciate your interest in Rilven Builders and we look forward to working together to bring your network infrastructure up to the best industry standards. The prices in this proposal are good for 90 days.</p>
    <div class="signed-label">SIGNED &amp; DATED</div>
    <div class="signed-rule"></div>
    <div class="sig-line" style="left:43px;top:130px;width:82px"></div>
    <div class="sig-line" style="left:170px;top:130px;width:83px"></div>
    <div class="sig-label" style="left:43px;top:132px">Customer Authorized Signature</div>
    <div class="sig-label" style="left:170px;top:132px">Date</div>
    <div class="sig-label signature" style="left:43px;top:159px;font-size:4.6px">Leo Marchetti</div>
    <div class="sig-line" style="left:43px;top:172px;width:82px"></div>
    <div class="sig-line" style="left:170px;top:172px;width:83px"></div>
    <div class="sig-label" style="left:43px;top:174px">Rilven Builders, Inc<br>Leo Marchetti</div>
    <div class="sig-label" style="left:170px;top:174px">Date</div>
    <div class="footer-bar"></div><div class="footer-tab"></div>
  </section>

  <section class="slide col-1 row-3">
    <div class="brand"><span class="brand-mark"></span><span class="brand-name">RILVEN BUILDERS</span></div>
    <div class="header-band"></div><div class="header-title">REFERENCES OF RECENT LOW VOLTAGE PROJECTS</div>
    <div class="accent-stripes"><span class="s-red"></span><span class="s-orange"></span><span class="s-yellow"></span><span class="s-green"></span></div>
    <div class="section-band" style="top:42px"></div>
    <div class="section-band-stripes" style="top:42px"><span class="s-green"></span><span class="s-yellow"></span><span class="s-orange"></span><span class="s-red"></span></div>
    <div class="band-label" style="left:48px;top:45px">Details</div>

    <div class="ref" style="left:48px;top:71px">
      <h5>Coastline Telecom Group</h5>
      <p class="i">Owen Carter</p>
      <p>Director, Business Coordinator</p>
      <p class="i">(555) 201-4830 | (555) 201-7712</p>
      <p class="i">owen@coastlinetelecom.example</p>
    </div>
    <div class="ref" style="left:168px;top:71px">
      <h5>Northgate Community School</h5>
      <p class="i">Adam Reyes</p>
      <p>IT Director</p>
      <p class="i">(555) 318-2294 | (555) 318-6650</p>
      <p class="i">areyes@northgate.example</p>
      <p class="i">410 Birchwood Avenue, Lakeshore, ST 10482</p>
    </div>
    <div class="ref" style="left:48px;top:117px">
      <h5>Bloomway Farms</h5>
      <p class="i">Marco Duarte</p>
      <p>IT Director</p>
      <p class="i">(555) 427-9031 | (555) 427-1180 Ext 210</p>
      <p class="i">mduarte@bloomway.example</p>
      <p class="i">88 Orchard Lane #12, Harborview, ST 10317</p>
    </div>
    <div class="ref" style="left:168px;top:117px">
      <h5>Brightpath Systems</h5>
      <p class="i">Neil Foster</p>
      <p>Director of Information Technology</p>
      <p class="i">(555) 630-4418 | (555) 630-9925</p>
      <p class="i">nfoster@brightpath.example</p>
      <p class="i">22 Market Square, Suite 5, Cedar Point, ST 10529</p>
    </div>
    <div class="client-strip">
      <span>Harbor Stay</span><span><i></i>Bean Corner</span><span>Callwise</span><span>Signalink</span><span>Maple Inns</span><span>Northline</span><span>Sandport</span><span><i></i>Greenleaf</span><span>Cedar Point City</span>
    </div>
    <div class="footer-bar"></div><div class="footer-tab"></div>
  </section>

  <section class="slide col-2 row-3">
    <div class="brand"><span class="brand-mark"></span><span class="brand-name">RILVEN BUILDERS</span></div>
    <div class="header-band"></div><div class="header-title">OUR RECENT PROJECTS</div>
    <div class="accent-stripes"><span class="s-red"></span><span class="s-orange"></span><span class="s-yellow"></span><span class="s-green"></span></div>
    <div class="project-grid">
      <div class="project-head">State Transit Office Building</div>
      <div class="project-head">Lakeshore County Health Dept</div>
      <div class="project-head">Vertex Data Center</div>
      <div class="project-head">Arcline Harborview</div>
      <div class="project-head">Signalink Flagship Store</div>
      <div class="project-head">Clearview Dermatology</div>
      <div class="project-photo ph-a" role="img" aria-label="Cable installation in a government office"></div>
      <div class="project-photo ph-b" role="img" aria-label="Network racks in a health department"></div>
      <div class="project-photo ph-c" role="img" aria-label="Data center aisle"></div>
      <div class="project-photo ph-c" role="img" aria-label="Open plan office workstations"></div>
      <div class="project-photo ph-d" role="img" aria-label="Retail store with purple lighting"></div>
      <div class="project-photo ph-e" role="img" aria-label="Patch panel with red cabling"></div>
      <div class="project-photo ph-a" role="img" aria-label="Server room cabling"></div>
      <div class="project-photo ph-b" role="img" aria-label="Rack being wired"></div>
      <div class="project-photo ph-e" role="img" aria-label="Data center rack with red cables"></div>
      <div class="project-photo ph-c" role="img" aria-label="Office floor cabling"></div>
      <div class="project-photo ph-f" role="img" aria-label="Cable tray with green patch cords"></div>
      <div class="project-photo ph-b" role="img" aria-label="Network cabinet"></div>
      <div class="project-photo ph-b" role="img" aria-label="Server cabinet install"></div>
      <div class="project-photo ph-b" role="img" aria-label="Racks in a data room"></div>
      <div class="project-photo ph-a" role="img" aria-label="Technician testing cabling"></div>
      <div class="project-photo ph-c" role="img" aria-label="Office desks with drops"></div>
      <div class="project-photo ph-d" role="img" aria-label="Ceiling cable runs in a store"></div>
      <div class="project-photo ph-a" role="img" aria-label="Finished patch panels"></div>
    </div>
    <div class="footer-bar"></div><div class="footer-tab"></div>
  </section>

  <section class="slide col-3 row-3">
    <div class="brand"><span class="brand-mark"></span><span class="brand-name">RILVEN BUILDERS</span></div>
    <div class="header-band"></div><div class="header-title">CERTIFICATION</div>
    <div class="accent-stripes"><span class="s-red"></span><span class="s-orange"></span><span class="s-yellow"></span><span class="s-green"></span></div>
    <p class="cert-copy">Rilven will certify the wiring to ensure/guarantee the performance and quality of cabling installation. Results will be provided to the customer at the completion of the installation. Copper Cable Certification Testing–The higher end CertiLine CX100 is the most sophisticated RF measurement engine in any handheld tester. Able to support up to 3GHz frequency range, and testing all mode combination parameters (including TCL), it exceeds the level 2G accuracy specifications for copper certification testing.</p>
    <div class="section-band" style="top:115px"></div>
    <div class="section-band-stripes" style="top:115px"><span class="s-red"></span><span class="s-orange"></span><span class="s-yellow"></span><span class="s-green"></span></div>
    <div class="band-label" style="left:46px;top:118px;font-size:4.4px">We Only Work With The Best</div>
    <div class="cert-intro">We are certified with the following top brands:</div>
    <div class="partner-row" style="top:141px"><span><i></i>Linwell</span><span>Conduix</span><span>Vantacore</span></div>
    <div class="partner-row" style="top:155px"><span>Probex</span><span>Sonaro</span><span>CablePro Guild</span></div>
    <div class="cert-photo" role="img" aria-label="Two handheld cable certification testers on a table"></div>
    <div class="footer-bar"></div><div class="footer-tab"></div>
  </section>
</main>
</body>
</html>
```